Flyer Design

We are a property company and need attractive flyers that will grab peoples attention. We want them to be bold but simple and not too busy. I attach a draft and also our logo. We will print in A5 size.
Thank you & I look forward to receiving designs.

It Company

```html
<!DOCTYPE html>
<html lang="en">
<head>
<meta charset="utf-8">
<title>Kora Developments Flyer</title>
<link rel="stylesheet" href="https://fonts.googleapis.com/css2?family=Roboto+Condensed:wght@700;800&family=Source+Sans+3:wght@400;600;700&display=swap">
<style>
  :root {
    --page-bg: #2f231c;
    --card-light: #e6ddcf;
    --card-mid: #dcd1bf;
    --card-dark: #d2c5b0;
    --ink-heading: #5a2823;
    --ink-body: #4b332c;
    --ink-muted: #5e4a42;
    --brand-mark: #a57a52;
    --brand-name: #8a5a36;
    --rule: #7a625a;
  }
  * { margin: 0; padding: 0; box-sizing: border-box; }
  html, body {
    width: 1200px;
    height: 964px;
    overflow: hidden;
    background: var(--page-bg);
  }
  .flyer {
    position: absolute;
    left: 40px;
    top: 87px;
    width: 1120px;
    height: 790px;
    background: linear-gradient(100deg, var(--card-dark) 0%, var(--card-light) 40%, var(--card-mid) 75%, var(--card-light) 100%);
    text-align: center;
    color: var(--ink-body);
  }
  .headline {
    position: absolute;
    left: 0; right: 0;
    top: 32px;
    font-family: "Roboto Condensed", "Arial Narrow", sans-serif;
    font-weight: 800;
    font-size: 38px;
    line-height: 51px;
    color: var(--ink-heading);
    letter-spacing: 0.3px;
  }
  .brand {
    position: absolute;
    left: 0; right: 0;
    top: 185px;
    display: flex;
    flex-direction: column;
    align-items: center;
  }
  .brand-square {
    width: 150px;
    height: 150px;
    background: var(--brand-mark);
  }
  .brand-name {
    margin-top: 105px;
    font-family: "Roboto Condensed", "Arial Narrow", sans-serif;
    font-weight: 700;
    font-size: 86px;
    line-height: 1;
    letter-spacing: 4px;
    text-transform: uppercase;
    color: var(--brand-name);
  }
  .question {
    position: absolute;
    left: 0; right: 0;
    top: 583px;
    font-family: "Roboto Condensed", "Arial Narrow", sans-serif;
    font-weight: 700;
    font-size: 34px;
    color: var(--ink-heading);
  }
  .service {
    position: absolute;
    left: 0; right: 0;
    top: 636px;
    font-family: "Source Sans 3", "Myriad Pro", sans-serif;
    font-weight: 600;
    font-size: 24px;
    color: var(--ink-body);
  }
  .divider {
    position: absolute;
    left: 96px;
    right: 104px;
    top: 682px;
    border-top: 1px solid var(--rule);
  }
  .contact {
    position: absolute;
    left: 0; right: 0;
    top: 692px;
    font-family: "Source Sans 3", "Myriad Pro", sans-serif;
    font-weight: 400;
    font-size: 21px;
    line-height: 30px;
    color: var(--ink-muted);
  }
  .contact .website {
    font-weight: 700;
    color: var(--ink-body);
    margin-left: 14px;
  }
</style>
</head>
<body>
  <main class="flyer">
    <h1 class="headline">Are you a homeowner looking for financial freedom<br>while been able to keep your own home?</h1>

    <div class="brand">
      <span class="brand-square" aria-hidden="true"></span>
      <p class="brand-name">Kora Developments</p>
    </div>

    <h2 class="question">ARE YOU STRUGGLING TO PAY YOUR MORTGAGE?</h2>
    <p class="service">KORA specialise in subdivisions including finance and management</p>

    <hr class="divider">

    <p class="contact">Call 021 555 0147 or email info@korasubdivisions.com for more information or to find out ifyour<br>property is suitable for subdivision in Auckland.<span class="website">www.KoraSubDivisions.com</span></p>
  </main>
</body>
</html>
```